Stationery Design Project

We need letterhead and business cards designed for our consulting firm. Color scheme, mostly deep blue (see logo). We are a commercial consulting work out firm, nationwide (large loans, $10MM and up). Visit our website for more info.
Updates

Project Deadline Extended
Reason: Meeting tomorrow morning to make final final decision. Would like this project to stay open to be able to provide feed back and receive final edits and approve. Thank you!!!

Target Market(s)

High end investors

Industry/Entity Type

Business

Requirements
Must have
• Letterhead must have the logo and the address

4817 Larkmoor Avenue, Suite 210, San Diego, CA 92107
Nice to have
• It would be nice to incorporate a watermark of all or some portion of the logo on the letterhead, or at least for the 2nd sheets.

Maybe our phone number: 858.555.0174
and/or webiste: www.tollandridgecap.example
Should not have
• Target users and audience of this will be men so, frilly or whimsical type designs are not preferred.

```html
<!DOCTYPE html>
<html lang="en">
<head>
<meta charset="utf-8">
<title>Tollandridge Capital Partners — Stationery</title>
<link rel="stylesheet" href="https://fonts.googleapis.com/css2?family=Arimo:wght@400;700&display=swap">
<style>
  :root {
    --sheet-light: #f2f2f2;
    --sheet-dark: #7a7a7a;
    --sky: #45bef0;
    --ink: #000000;
    --paper: #fbfcfd;
    --silver: #a9adb3;
    --silver-faint: #dfe3e8;
    --white: #ffffff;
  }
  * { box-sizing: border-box; margin: 0; padding: 0; }
  html, body { width: 777px; height: 1200px; overflow: hidden; }
  body {
    position: relative;
    font-family: "Arimo", Arial, sans-serif;
    background: linear-gradient(225deg, var(--sheet-light) 0%, #c4c4c4 45%, var(--sheet-dark) 100%);
    color: var(--ink);
  }
  .abs { position: absolute; }

  .brand-name {
    font-family: "Arimo", Arial, sans-serif;
    font-weight: 400;
    color: var(--silver);
    text-align: center;
    letter-spacing: 2px;
    white-space: nowrap;
    line-height: 1.15;
  }
  .brand-mark { display: inline-block; background: var(--silver); vertical-align: middle; }

  .hero-brand { left: 243px; top: 30px; width: 300px; }
  .hero-brand .brand-mark { width: 26px; height: 26px; margin-bottom: 10px; }
  .hero-brand .brand-name { font-size: 30px; }
  .hero-brand .brand-sub { font-size: 12px; letter-spacing: 6px; }

  .section-label { font-size: 16px; color: var(--ink); }
  .label-card { left: 130px; top: 146px; }
  .label-letter { left: 93px; top: 337px; }

  .card { top: 169px; width: 247px; height: 142px; overflow: hidden; }
  .card-front { left: 126px; background: var(--ink); }
  .card-back { left: 385px; background: var(--sky); border: 1px solid #6d7a82; }

  .card-front .brand { left: 8px; top: 48px; width: 218px; }
  .card-front .brand-name { font-size: 19px; }
  .card-front .brand-sub { font-size: 8px; letter-spacing: 3px; }
  .card-front .brand-mark { width: 14px; height: 14px; margin-bottom: 6px; }

  .spine {
    font-weight: 700; font-size: 19px; letter-spacing: 0;
    white-space: nowrap; transform-origin: left top;
  }
  .card-front .spine { left: 218px; top: 142px; transform: rotate(-90deg); color: var(--white); }
  .card-back .spine { left: 1px; top: 142px; transform: rotate(-90deg); color: var(--ink); }

  .contact-block { left: 89px; top: 42px; font-size: 9px; line-height: 10.8px; color: #111; }
  .contact-block .firm { font-size: 11px; line-height: 12px; }
  .contact-block .firm-sub { font-size: 4px; line-height: 6px; padding-left: 15px; }
  .contact-block .indent { padding-left: 43px; }

  .letterhead { left: 92px; top: 362px; width: 600px; height: 777px; background: var(--sky); border: 1px solid #6d7a82; }
  .letter-body { left: 19px; top: 26px; width: 562px; height: 664px; background: var(--paper); border: 1px solid #6d7a82; border-radius: 24px; }
  .letter-tab { left: 169px; top: 12px; width: 247px; height: 141px; background: var(--ink); border-radius: 32px; }
  .letter-tab .brand { left: 0; top: 52px; width: 247px; }
  .letter-tab .brand-name { font-size: 19px; }
  .letter-tab .brand-sub { font-size: 8px; letter-spacing: 3px; }
  .letter-tab .brand-mark { width: 14px; height: 14px; margin-bottom: 6px; }

  .watermark { left: 0; top: 318px; width: 562px; }
  .watermark .brand-name { color: var(--silver-faint); font-size: 32px; }
  .watermark .brand-sub { color: var(--silver-faint); font-size: 12px; letter-spacing: 7px; }
  .watermark .brand-mark { width: 28px; height: 28px; background: var(--silver-faint); margin-bottom: 12px; }

  .letter-footer { left: 0; top: 709px; width: 600px; text-align: center; font-size: 9px; line-height: 10.8px; color: #111; }
  .letter-footer .firm { font-size: 14px; line-height: 15px; }
  .letter-footer .firm-sub { font-size: 4px; line-height: 6px; }
</style>
</head>
<body>

  <header class="abs hero-brand">
    <div class="brand-name"><span class="brand-mark"></span></div>
    <div class="brand-name">TOLLANDRIDGE</div>
    <div class="brand-name brand-sub">CAPITAL PARTNERS</div>
  </header>

  <div class="abs section-label label-card">BUSINESS CARD</div>

  <section class="abs card card-front">
    <div class="abs brand">
      <div class="brand-name"><span class="brand-mark"></span></div>
      <div class="brand-name">TOLLANDRIDGE</div>
      <div class="brand-name brand-sub">CAPITAL PARTNERS</div>
    </div>
    <div class="abs spine">TOLLANDRIDGE</div>
  </section>

  <section class="abs card card-back">
    <div class="abs spine">TOLLANDRIDGE</div>
    <address class="abs contact-block" style="font-style:normal">
      <div class="firm">TOLLANDRIDGE</div>
      <div class="firm-sub">CAPITAL PARTNERS</div>
      <div>Address : 4817 Larkmoor Avenue,</div>
      <div class="indent">Suite 210,</div>
      <div class="indent">San Diego,</div>
      <div class="indent">CA 92107</div>
      <div>phone number: 858.555.0174</div>
      <div>Email: info@tollandridgecap.example</div>
      <div>webiste: www.tollandridgecap.example</div>
    </address>
  </section>

  <div class="abs section-label label-letter">LETTER HEAD</div>

  <section class="abs letterhead">
    <div class="abs letter-body">
      <div class="abs watermark" aria-hidden="true">
        <div class="brand-name"><span class="brand-mark"></span></div>
        <div class="brand-name">TOLLANDRIDGE</div>
        <div class="brand-name brand-sub">CAPITAL PARTNERS</div>
      </div>
    </div>
    <div class="abs letter-tab">
      <div class="abs brand">
        <div class="brand-name"><span class="brand-mark"></span></div>
        <div class="brand-name">TOLLANDRIDGE</div>
        <div class="brand-name brand-sub">CAPITAL PARTNERS</div>
      </div>
    </div>
    <address class="abs letter-footer" style="font-style:normal">
      <div class="firm">TOLLANDRIDGE</div>
      <div class="firm-sub">CAPITAL PARTNERS</div>
      <div>Address : 4817 Larkmoor Avenue, Suite 210, San Diego, CA 92107</div>
      <div>phone number: 858.555.0174</div>
      <div>Email: info@tollandridgecap.example</div>
      <div>webiste: www.tollandridgecap.example</div>
    </address>
  </section>

</body>
</html>
```